HarborRise Summer Brunch

This flyer is designed to market the upcoming conference in July

Target Market(s)

African American Christian Men and Women

Font styles to use
Decorative

Requirements
Must have
• This flyer is to represent both men and women as follows:
• Although offered on the same day and same location - Men and Women must appear two meetings in one location
• 1. BOS - Brothers of Steel
• 2. GRVW - Grounded and Rooted in Virtue and Worth - Women
• Theme: "2020 - Walking With Courage" (Ephesians 6:10-15)
• Date: June 27, 2020
Nice to have
• *Distinct between the two meetings in one
• * Unified brand coupled with Men and Women targets
• * Vibrant, energized, active flyer to communicate promise and hope
Should not have
• Profanity, clip art, etc.

```html
<!DOCTYPE html>
<html lang="en">
<head>
<meta charset="utf-8">
<title>HarborRise Summer Brunch – Flyer Design</title>
<link href="https://fonts.googleapis.com/css2?family=Montserrat:ital,wght@0,500;0,600;0,800;1,400&family=Oswald:wght@400&family=Playfair+Display:wght@700;900&display=swap" rel="stylesheet">
<style>
:root{
  --board:#2e2e2e;
  --board-text:#e6e6e6;
  --gold-dark:#9a6a14;
  --gold:#c9961f;
  --gold-light:#f6dc7a;
  --gold-text:#b07d1a;
  --ink:#1d1d1d;
  --paper:#ffffff;
  --marble:#f1efec;
}
*{margin:0;padding:0;box-sizing:border-box}
html,body{width:1200px;height:920px;overflow:hidden;background:var(--board)}
.board{position:relative;width:1200px;height:920px;background:var(--board);font-family:'Montserrat',sans-serif}
.board-title{position:absolute;left:47px;top:34px;display:flex;align-items:baseline;gap:14px;color:var(--board-text)}
.board-title__main{font-weight:800;font-size:56px;letter-spacing:1px}
.board-title__sub{font-style:italic;font-weight:400;font-size:27px}
.flyer{position:absolute;top:114px;width:536px;height:758px;overflow:hidden;background:var(--marble)}
.flyer--split{left:45px}
.flyer--light{left:621px}
.gold-band{position:absolute;left:0;width:100%;height:22px;
  background:linear-gradient(180deg,var(--gold-light) 0%,var(--gold) 45%,var(--gold-dark) 70%,var(--gold-light) 100%);z-index:3}
.gold-band--top{top:0}
.gold-band--bottom{bottom:0}
.backdrop{position:absolute;left:0;top:0;width:100%;height:100%}
.brand{position:absolute;font-family:'Playfair Display',serif;font-weight:900;color:var(--gold-text);line-height:1;z-index:2}
.brand__name{font-size:52px;letter-spacing:2px}
.brand__full{font-size:13px;margin-top:-4px;letter-spacing:.2px;white-space:nowrap}
.brand--right{text-align:right}
.org{position:absolute;width:230px;text-align:center;color:var(--ink);z-index:2}
.org__name{font-family:'Playfair Display',serif;font-weight:700;font-size:28px;line-height:1}
.org__tagline{font-family:'Montserrat',sans-serif;font-weight:600;font-size:7.5px;letter-spacing:.6px;margin-top:5px;white-space:nowrap}
.emblem{position:absolute;left:0;top:0;width:100%;height:100%;z-index:1}
.event{position:absolute;left:0;width:100%;text-align:center;z-index:2}
.event__year{font-family:'Playfair Display',serif;font-weight:900;font-size:72px;line-height:1;color:var(--gold-text)}
.event__theme{font-family:'Oswald',sans-serif;font-size:29px;color:var(--gold-text);line-height:1.1}
.event__verse{font-family:'Montserrat',sans-serif;font-weight:500;font-size:15px;color:var(--ink);margin-top:6px}
.event__time{font-family:'Oswald',sans-serif;font-size:29px;color:var(--gold-text);margin-top:6px}
.date-badge{position:absolute;text-align:center;font-family:'Oswald',sans-serif;color:#6b4406;line-height:1;z-index:2}
.date-badge__day{font-size:21px}
.date-badge__year{font-size:34px}
</style>
</head>
<body>
<div class="board">
  <div class="board-title"><span class="board-title__main">PREVIEW</span><span class="board-title__sub">Flyer Design</span></div>

  <!-- Split version -->
  <section class="flyer flyer--split">
    <svg class="backdrop" viewBox="0 0 536 758" role="img" aria-label="Dark slate marble with gold veins above, white marble with gold veins below">
      <defs>
        <linearGradient id="whiteMarble" x1="0" y1="0" x2="1" y2="1">
          <stop offset="0" stop-color="#f7f6f4"/><stop offset=".5" stop-color="#eeebe6"/><stop offset=".8" stop-color="#f3ead0"/><stop offset="1" stop-color="#faf8f4"/>
        </linearGradient>
        <linearGradient id="darkMarble" x1="0" y1="0" x2="1" y2="1">
          <stop offset="0" stop-color="#34373c"/><stop offset=".5" stop-color="#4a4d52"/><stop offset="1" stop-color="#2c2e32"/>
        </linearGradient>
      </defs>
      <rect width="536" height="758" fill="url(#whiteMarble)"/>
      <polygon points="0,0 536,0 536,305 0,516" fill="url(#darkMarble)"/>
    </svg>
    <div class="gold-band gold-band--top"></div>

    <svg class="emblem" viewBox="0 0 536 758" aria-hidden="true">
      <defs>
        <linearGradient id="ringGold" x1="0" y1="0" x2="1" y2="1">
          <stop offset="0" stop-color="#f6dc7a"/><stop offset=".4" stop-color="#c9961f"/><stop offset=".7" stop-color="#8a5c0f"/><stop offset="1" stop-color="#f0cf6a"/>
        </linearGradient>
        <radialGradient id="discGold" cx=".4" cy=".35" r=".7">
          <stop offset="0" stop-color="#fbe58e"/><stop offset=".6" stop-color="#deae38"/><stop offset="1" stop-color="#a8761a"/>
        </radialGradient>
      </defs>
      <circle cx="265" cy="391" r="148" fill="url(#ringGold)"/>
      <circle cx="265" cy="391" r="136" fill="none" stroke="#7a510c" stroke-width="2"/>
      <circle cx="265" cy="391" r="128" fill="var(--paper)"/>
      <circle cx="265" cy="257" r="58" fill="#8a5c0f"/>
      <circle cx="265" cy="257" r="55" fill="url(#discGold)"/>
    </svg>
    <div class="date-badge" style="left:215px;top:226px;width:100px"><div class="date-badge__day">June 27</div><div class="date-badge__year">2020</div></div>
    <div class="event" style="top:325px">
      <div class="event__year">2020</div>
      <div class="event__theme">Walking With Courage</div>
      <div class="event__verse">Ephesians 6:10-15</div>
      <div class="event__time">10am</div>
    </div>

    <div class="brand" style="left:41px;top:56px"><div class="brand__name">BOS</div><div class="brand__full">Brothers of Steel</div></div>
    <div class="brand" style="left:41px;top:650px;width:250px"><div class="brand__name">GRVW</div><div class="brand__full" style="font-size:9px">Grounded and Rooted in Virtue and Worth</div></div>
    <div class="org" style="left:302px;top:672px"><div class="org__name">HarborRise</div><div class="org__tagline">LIFTING HEARTS, BUILDING NEIGHBORHOODS</div></div>
    <div class="gold-band gold-band--bottom"></div>
  </section>

  <!-- Light version -->
  <section class="flyer flyer--light">
    <svg class="backdrop" viewBox="0 0 536 758" role="img" aria-label="White marble with soft gold veins and a burst of gold dots around the centre">
      <defs>
        <linearGradient id="lightMarble" x1="0" y1="0" x2="1" y2="1">
          <stop offset="0" stop-color="#fbfaf8"/><stop offset=".5" stop-color="#f1eee9"/><stop offset="1" stop-color="#f7f2e3"/>
        </linearGradient>
        <radialGradient id="goldBurst" cx="268" cy="391" r="300" gradientUnits="userSpaceOnUse">
          <stop offset="0" stop-color="#e2b54a" stop-opacity=".75"/><stop offset=".5" stop-color="#e7c062" stop-opacity=".4"/><stop offset="1" stop-color="#f4e3b0" stop-opacity="0"/>
        </radialGradient>
      </defs>
      <rect width="536" height="758" fill="url(#lightMarble)"/>
      <ellipse cx="268" cy="391" rx="300" ry="320" fill="url(#goldBurst)"/>
    </svg>
    <div class="gold-band gold-band--top"></div>

    <svg class="emblem" viewBox="0 0 536 758" aria-hidden="true">
      <defs>
        <radialGradient id="discGold2" cx=".4" cy=".35" r=".7">
          <stop offset="0" stop-color="#fbe58e"/><stop offset=".6" stop-color="#deae38"/><stop offset="1" stop-color="#a8761a"/>
        </radialGradient>
      </defs>
      <polygon points="268,258 396,324 396,454 268,520 140,454 140,324" fill="#c9961f" opacity=".5"/>
      <polygon points="268,264 392,327 392,453 268,516 144,453 144,327" fill="var(--paper)" stroke="#c9961f" stroke-width="1.5"/>
      <circle cx="268" cy="248" r="50" fill="#8a5c0f"/>
      <circle cx="268" cy="248" r="47" fill="url(#discGold2)"/>
    </svg>
    <div class="date-badge" style="left:218px;top:221px;width:100px"><div class="date-badge__day" style="font-size:19px">June 27</div><div class="date-badge__year" style="font-size:31px">2020</div></div>
    <div class="event" style="top:308px">
      <div class="event__year" style="font-size:70px">2020</div>
      <div class="event__theme">Walking With Courage</div>
      <div class="event__verse">Ephesians 6:10-15</div>
      <div class="event__time">10am</div>
    </div>

    <div class="brand" style="left:29px;top:52px"><div class="brand__name" style="font-size:44px">BOS</div><div class="brand__full" style="font-size:12px">Brothers of Steel</div></div>
    <div class="brand brand--right" style="right:22px;top:52px;width:230px"><div class="brand__name" style="font-size:44px">GRVW</div><div class="brand__full" style="font-size:8.5px">Grounded and Rooted in Virtue and Worth</div></div>
    <div class="org" style="left:153px;top:672px"><div class="org__name">HarborRise</div><div class="org__tagline">LIFTING HEARTS, BUILDING NEIGHBORHOODS</div></div>
    <div class="gold-band gold-band--bottom"></div>
  </section>
</div>
</body>
</html>
```